Plumbing Product Supply Company Needs Front & Back Cover Design For Instruction Manuals

We need a front and back over design for our instruction manuals that we need to give to clients.

There will also be a picture of the product on the front cover so please use the supplied image as dummy.

it needs to incorporate our logo and branding colours.

We are the industry leader so it needs to be up-market, professional and stand out from the crowd.

Target Market(s)

Plumbing Companies

Industry/Entity Type

Plumbing

Font styles to use
Sans Serif

Colors
abd036
ffffff
000000
eaeaea
cbcbcb

Requirements
Must have
• Front & Back Cover as it will become a booklet.
• The logo is to be on the black background.
Nice to have
• Professional, modern, sleek.
Should not have
• Other colours that what is on the guidelines.

```html
<!DOCTYPE html>
<html lang="en">
<head>
<meta charset="utf-8">
<title>Kestrel Pipeline Supplies – Manual Cover Spread</title>
<link href="https://fonts.googleapis.com/css2?family=Jost:wght@400;500;600&family=Lato:wght@400;700&display=swap" rel="stylesheet">
<style>
  :root {
    --brand-green: #abd036;
    --brand-green-dark: #6f8f1f;
    --black: #000000;
    --white: #ffffff;
    --light-grey: #eaeaea;
    --mid-grey: #cbcbcb;
    --stage: #2b2b2b;
  }
  html, body {
    margin: 0;
    padding: 0;
    width: 1200px;
    height: 789px;
    overflow: hidden;
    background: var(--stage);
  }
  .spread {
    position: absolute;
    left: 77px;
    top: 24px;
    width: 1046px;
    height: 740px;
    display: flex;
    box-shadow: 0 10px 30px rgba(0,0,0,0.5);
  }
  .cover {
    position: relative;
    width: 523px;
    height: 740px;
    overflow: hidden;
    background: linear-gradient(180deg, var(--white) 0%, var(--light-grey) 100%);
  }
  .cover svg.cover-art {
    position: absolute;
    inset: 0;
  }
  .brand-name {
    position: absolute;
    left: 0;
    right: 0;
    text-align: center;
    margin: 0;
    font-family: "Jost", sans-serif;
    font-weight: 500;
    color: var(--brand-green);
    text-transform: uppercase;
    letter-spacing: 0.12em;
    line-height: 1.25;
  }
  .cover--back .brand-name {
    top: 300px;
    font-size: 24px;
  }
  .cover--front .brand-name {
    top: 52px;
    font-size: 30px;
  }
  .product-photo {
    position: absolute;
    left: 86px;
    top: 300px;
    width: 350px;
    height: 270px;
    border-radius: 6px;
    background: radial-gradient(ellipse at 50% 45%, #8a8a8a 0%, #4d4d4d 45%, #d9d9d9 80%, var(--light-grey) 100%);
  }
  .contact {
    position: absolute;
    left: 0;
    right: 0;
    top: 615px;
    text-align: center;
    font-family: "Lato", sans-serif;
    color: var(--black);
  }
  .contact__title {
    margin: 0 0 6px;
    font-size: 17px;
    font-weight: 700;
  }
  .contact__line {
    margin: 0;
    font-size: 10px;
    line-height: 1.5;
  }
</style>
</head>
<body>
  <main class="spread">
    <section class="cover cover--back" aria-label="Back cover">
      <svg class="cover-art" width="523" height="740" viewBox="0 0 523 740" aria-hidden="true">
        <defs>
          <linearGradient id="backSwoosh" x1="0" y1="0" x2="1" y2="0">
            <stop offset="0" stop-color="#6f8f1f"/>
            <stop offset="0.5" stop-color="#abd036"/>
            <stop offset="1" stop-color="#6f8f1f"/>
          </linearGradient>
        </defs>
        <path d="M0 0 H523 V420 C420 440 300 470 200 520 C130 555 60 590 0 600 Z" fill="#abd036"/>
        <path d="M0 0 H523 V400 C410 420 290 455 190 505 C120 540 55 572 0 580 Z" fill="url(#backSwoosh)"/>
        <path d="M0 0 H523 V392 C400 405 280 440 180 492 C110 528 50 555 0 562 Z" fill="#000"/>
        <path d="M523 440 C420 455 300 490 210 540 C300 505 420 470 523 458 Z" fill="#abd036" opacity="0.85"/>
        <path d="M0 640 C60 615 120 590 170 565 C120 600 60 625 0 650 Z" fill="#000"/>
      </svg>
      <p class="brand-name">Kestrel<br>Pipeline Supplies</p>
      <div class="contact">
        <p class="contact__title">Contact Us:</p>
        <p class="contact__line">Lorem ipsum Lorem ipsum Lorem ipsum Lorem ipsum Lorem ipsum</p>
        <p class="contact__line">Email: youremail@mailbox.com | Ph: 000 000 0000 | Fax: 000 000 0000</p>
      </div>
    </section>

    <section class="cover cover--front" aria-label="Front cover">
      <svg class="cover-art" width="523" height="740" viewBox="0 0 523 740" aria-hidden="true">
        <defs>
          <linearGradient id="frontSwoosh" x1="0" y1="0" x2="1" y2="0">
            <stop offset="0" stop-color="#6f8f1f"/>
            <stop offset="0.5" stop-color="#abd036"/>
            <stop offset="1" stop-color="#6f8f1f"/>
          </linearGradient>
        </defs>
        <path d="M0 0 H523 V150 C440 200 330 240 220 245 C140 248 60 235 0 215 Z" fill="#abd036"/>
        <path d="M0 0 H523 V130 C440 180 330 222 220 228 C140 232 60 220 0 200 Z" fill="url(#frontSwoosh)"/>
        <path d="M0 0 H523 V118 C435 168 325 208 215 214 C135 218 60 205 0 188 Z" fill="#000"/>
        <path d="M523 170 C450 215 360 250 260 262 C360 240 450 205 523 185 Z" fill="#abd036" opacity="0.85"/>
      </svg>
      <p class="brand-name">Kestrel<br>Pipeline Supplies</p>
      <div class="product-photo" role="img" aria-label="Product photograph: pipelining kit with case, resin containers, liner rolls, air hose, inversion hoses and green push rods"></div>
    </section>
  </main>
</body>
</html>
```